Can you design a business card design? Looking for something unique and different. Can you design a business card design? Looking for something unique and different.Can you design a business card design? Looking for something unique and different.Can you design a business card design? Looking for something unique and different.Can you design a business card design? Looking for something unique and different.Can you design a business card design? Looking for something unique and different.

Industry/Entity Type

Business

Contact Information for Business Card

Can you design a business card design? Looking for something unique and different.

Font styles to use
Serif

```html
<!DOCTYPE html>
<html lang="en">
<head>
<meta charset="utf-8">
<title>Dosewell Business Card</title>
<link href="https://fonts.googleapis.com/css2?family=Lato:wght@400;700&display=swap" rel="stylesheet">
<style>
  :root {
    --backdrop: #3a302b;
    --card: #111012;
    --card-edge: #1c1b1e;
    --lilac: #a585c4;
    --lilac-soft: #9b7fb8;
    --text: #f1eff3;
    --silver: #d4d4d6;
    --divider: #2c2a2f;
  }
  * { box-sizing: border-box; margin: 0; padding: 0; }
  html, body {
    width: 1200px; height: 844px; overflow: hidden;
    background: var(--backdrop);
    font-family: "Lato", sans-serif;
  }
  .stage {
    position: relative; width: 1200px; height: 844px;
    display: flex; align-items: center; justify-content: center; gap: 60px;
  }
  .card {
    width: 520px; height: 298px;
    background: var(--card);
    border: 1px solid var(--card-edge);
    box-shadow: 0 18px 40px rgba(0,0,0,.45);
    position: relative;
  }
  .card-front { display: flex; }
  .brand-panel {
    width: 50%;
    display: flex; align-items: center; justify-content: center; gap: 12px;
  }
  .brand-mark {
    width: 18px; height: 18px; background: var(--lilac);
  }
  .brand-name {
    color: var(--lilac); font-weight: 700; font-size: 34px; letter-spacing: .5px;
  }
  .contact-panel {
    width: 50%;
    border-left: 1px solid var(--divider);
    padding: 48px 0 0 26px;
    color: var(--text);
    font-size: 15px; line-height: 1.3;
  }
  .person-name { color: var(--lilac); font-size: 20px; }
  .person-role { margin-bottom: 14px; }
  .address { margin-bottom: 14px; }
  .contact-line .label { color: var(--lilac-soft); display: inline-block; width: 18px; }
  .card-back {
    display: flex; align-items: center; justify-content: center;
  }
  .back-name {
    color: var(--silver); font-weight: 700; font-size: 58px; letter-spacing: 1px;
  }
</style>
</head>
<body>
<main class="stage">
  <section class="card card-front">
    <div class="brand-panel">
      <span class="brand-mark"></span>
      <span class="brand-name">Dosewell</span>
    </div>
    <div class="contact-panel">
      <p class="person-name">Marcus Hale</p>
      <p class="person-role">Managing Director</p>
      <p class="address">48 Harbour Lane,<br>Northfield, 204170.</p>
      <p class="contact-line"><span class="label">T:</span> 044-555 010 221</p>
      <p class="contact-line"><span class="label">E:</span> hello@dosewell.co</p>
      <p class="contact-line"><span class="label">W:</span>www.dosewell-care.com</p>
    </div>
  </section>
  <section class="card card-back">
    <span class="back-name">Dosewell</span>
  </section>
</main>
</body>
</html>
```